New business card for my lawn and landscape business

Hollin Yard and Building is a full-service lawn care, landscaping, and light construction company serving Paragould and the Northeast Arkansas region. The business is owned and operated by Dorian Waltham, with a reputation for hands-on, detail-oriented service, dependable crews, and quality results for both residential and commercial clients. A well regarded business with great reviews.
Owner Dorian Waltham
Hollinyardandbuilding.example

Target Market(s)

Commercial, Middle, and upper class in north east Arkansas

Industry/Entity Type

Lawn maintenance and landscape

Contact Information for Business Card

Hollin Yard And Building Professional lawn care, landscaping, and property improvement in Northeast Arkansas. • lawn maintenance •lawn treatments and weed control • exterior projects • Custom landscape design & installation • Sod, trees, rock & drainage solutions • Residential & commercial services Reliable. Detailed. Done right.

Requirements
Must have
• Business name, service area, list of some of our services, clean design that represents
Nice to have
• Unique. Different design element than just grass because its already in n the logo. Picture of a warm season (south) lawn or landscape. Pictures of the type of work we do

```html
<!DOCTYPE html>
<html lang="en">
<head>
<meta charset="utf-8">
<title>Hollin Yard and Building – Business Card</title>
<link rel="stylesheet" href="https://fonts.googleapis.com/css2?family=Tinos:wght@400;700&display=swap">
<style>
  :root {
    --backdrop: #8e8e90;
    --card-white: #ffffff;
    --brand-green: #7ab342;
    --ink: #1a1a1a;
    --ink-soft: #6f6f6f;
    --on-green: #ffffff;
  }
  * { box-sizing: border-box; margin: 0; padding: 0; }
  html, body { width: 1200px; height: 1200px; overflow: hidden; }
  body {
    background: var(--backdrop);
    font-family: "Tinos", "Times New Roman", serif;
    display: flex;
    flex-direction: column;
    align-items: center;
    justify-content: center;
    gap: 60px;
  }
  .card {
    position: relative;
    width: 900px;
    height: 514px;
    background: var(--card-white);
    overflow: hidden;
  }
  .card__shape { position: absolute; inset: 0; width: 100%; height: 100%; }
  .card__shape path { fill: var(--brand-green); }

  /* Front: services + wordmark */
  .services {
    position: absolute;
    left: 40px;
    top: 50%;
    transform: translateY(-50%);
    list-style: none;
    color: var(--on-green);
    font-size: 20px;
    line-height: 26px;
  }
  .services li::before { content: "• "; }

  .wordmark {
    position: absolute;
    display: flex;
    align-items: center;
    color: var(--ink-soft);
    font-weight: 400;
  }
  .wordmark__dot {
    flex: none;
    border-radius: 50%;
    background: var(--brand-green);
  }
  .wordmark--large {
    left: 560px;
    top: 50%;
    transform: translateY(-50%);
    gap: 16px;
    font-size: 30px;
    line-height: 36px;
    width: 320px;
  }
  .wordmark--large .wordmark__dot { width: 44px; height: 44px; }

  /* Back: owner + contact */
  .owner {
    position: absolute;
    left: 44px;
    top: 218px;
    color: var(--ink);
  }
  .owner__name { font-size: 26px; line-height: 30px; }
  .owner__name strong { font-weight: 700; }
  .owner__title { font-size: 21px; line-height: 28px; }

  .wordmark--small {
    left: 44px;
    bottom: 48px;
    gap: 8px;
    font-size: 14px;
    line-height: 16px;
    width: 160px;
  }
  .wordmark--small .wordmark__dot { width: 22px; height: 22px; }

  .website {
    position: absolute;
    right: 40px;
    top: 242px;
    display: flex;
    align-items: center;
    gap: 18px;
    color: var(--on-green);
    font-size: 22px;
  }
  .website svg { width: 26px; height: 26px; }

  .tagline {
    position: absolute;
    right: 40px;
    bottom: 34px;
    width: 420px;
    text-align: right;
    color: var(--on-green);
    font-size: 16px;
    line-height: 21px;
  }
</style>
</head>
<body>

  <section class="card card--front" aria-label="Business card front">
    <svg class="card__shape" viewBox="0 0 900 514" preserveAspectRatio="none" aria-hidden="true">
      <path d="M0 0 H415 C505 130 505 384 415 514 H0 Z"/>
    </svg>
    <ul class="services">
      <li>lawn maintenance</li>
      <li>lawn treatments and weed control</li>
      <li>exterior projects</li>
      <li>Custom landscape design &amp; installation</li>
      <li>Sod, trees, rock &amp; drainage solutions</li>
      <li>Residential &amp; commercial services Reliable</li>
    </ul>
    <div class="wordmark wordmark--large">
      <span class="wordmark__dot" aria-hidden="true"></span>
      <span class="wordmark__name">Hollin Yard and Building</span>
    </div>
  </section>

  <section class="card card--back" aria-label="Business card back">
    <svg class="card__shape" viewBox="0 0 900 514" preserveAspectRatio="none" aria-hidden="true">
      <path d="M485 0 H900 V514 H485 C395 384 395 130 485 0 Z"/>
    </svg>
    <div class="owner">
      <p class="owner__name"><strong>Dorian</strong> Waltham</p>
      <p class="owner__title">Owner</p>
    </div>
    <div class="wordmark wordmark--small">
      <span class="wordmark__dot" aria-hidden="true"></span>
      <span class="wordmark__name">Hollin Yard and Building</span>
    </div>
    <p class="website">
      <span>Hollinyardandbuilding.example</span>
      <svg viewBox="0 0 24 24" fill="none" stroke="currentColor" stroke-width="2" aria-hidden="true">
        <circle cx="12" cy="12" r="10"/>
        <path d="M2 12h20M12 2c3 3 4 6.5 4 10s-1 7-4 10M12 2c-3 3-4 6.5-4 10s1 7 4 10"/>
      </svg>
    </p>
    <p class="tagline">Hollin Yard And Building Professional lawn care, landscaping, and property improvement in Northeast Arkansas.</p>
  </section>

</body>
</html>
```